Need a plumber

Would like a postcard sized flyer made up. Want the design to be kept very simple.
List of services we carry out in bullet point or similar.
Phone number and email included on the flyer.
Logo to feature prominantly.

List of services: Hot water issues
Burst Pipes
Gas Plumbing
Roof leaks
Drain blockages

Target Market(s)

Mums, dads and hosehgold owners

Industry/Entity Type

Plumbing

Colors
0054AA
0677BA
7BADD7
CADEEF
E8F1F8

Requirements
Must have
• Services we off and our logo, also must say "local plumber"

```html
<!DOCTYPE html>
<html lang="en">
<head>
<meta charset="utf-8">
<title>Clearflow Plumbing Solutions – Flyer</title>
<link rel="stylesheet" href="https://fonts.googleapis.com/css2?family=Bebas+Neue&family=Roboto:ital,wght@0,300;0,500;1,900&family=Roboto+Condensed:wght@400&family=Russo+One&display=swap">
<style>
  :root{
    --ink:#0d0d0f;
    --ink-soft:#1c1c20;
    --cyan:#00c8ff;
    --grey:#e4e4e6;
    --white:#ffffff;
    --logo-ink:#111111;
    --pipe-blue:#1a8fd8;
    --pipe-grey:#cfd3d6;
    --mascot-blue:#2f7fb5;
    --mascot-light:#8cc0de;
  }
  *{margin:0;padding:0;box-sizing:border-box}
  html,body{width:963px;height:1200px;overflow:hidden;background:var(--ink)}
  .flyer{position:relative;width:963px;height:1200px;overflow:hidden;
    background:radial-gradient(ellipse at 40% 40%,var(--ink-soft),var(--ink) 75%)}
  .shapes{position:absolute;inset:0;width:963px;height:1200px}
  .headline{position:absolute;left:84px;font-family:"Bebas Neue",sans-serif;line-height:1;color:var(--white);white-space:nowrap}
  .headline--top{top:104px;font-size:104px;letter-spacing:-1px}
  .headline--accent{top:190px;font-size:170px;color:var(--cyan);letter-spacing:-2px}
  .headline--bottom{top:334px;font-size:146px;letter-spacing:-1px}
  .address{position:absolute;left:87px;top:490px;display:flex;gap:20px;align-items:flex-start}
  .address p{font-family:"Roboto",sans-serif;font-weight:300;font-size:27px;line-height:31px;color:var(--white)}
  .pictorial{position:absolute}
  .pictorial--pipes{left:598px;top:0;width:365px;height:225px;
    background:linear-gradient(160deg,var(--pipe-blue) 0%,#4cb6ef 45%,var(--pipe-grey) 80%);border-radius:0 0 0 120px}
  .pictorial--mascot{left:560px;top:300px;width:403px;height:560px;
    background:radial-gradient(circle at 60% 50%,var(--mascot-light),var(--mascot-blue) 70%);border-radius:200px 0 0 200px}
  .call{position:absolute;left:69px;top:645px;color:var(--white);font-family:"Roboto",sans-serif;font-style:italic;font-weight:900}
  .call__label{display:flex;align-items:center;gap:8px;font-size:46px;line-height:46px;padding-left:6px}
  .call__number{font-size:47px;line-height:50px;margin-top:4px}
  .services{position:absolute;left:82px;top:806px}
  .services h2{font-family:"Russo One",sans-serif;font-weight:400;font-size:24px;letter-spacing:6px;color:var(--cyan);line-height:28px}
  .services ul{list-style:none;margin-top:18px}
  .services li{display:flex;align-items:center;gap:22px;height:40px;font-family:"Roboto",sans-serif;font-weight:500;font-size:25px;color:var(--white)}
  .services li.more{padding-left:49px}
  .logo{position:absolute;left:583px;top:751px;width:328px;height:328px;border-radius:50%;background:var(--white);
    display:flex;flex-direction:column;align-items:center;justify-content:center;text-align:center}
  .logo span{font-family:"Roboto",sans-serif;font-weight:500;font-size:34px;letter-spacing:5px;color:var(--logo-ink);line-height:44px}
  .footer{position:absolute;left:0;top:1102px;width:963px;height:51px;display:flex;align-items:center;justify-content:center;
    font-family:"Roboto Condensed",sans-serif;font-size:18px;color:var(--ink)}
  .footer__item{display:flex;align-items:center;gap:12px;padding:0 16px}
  .footer__divider{width:1px;height:34px;background:rgba(0,0,0,.35)}
</style>
</head>
<body>
<main class="flyer">
  <svg class="shapes" viewBox="0 0 1438 1860" preserveAspectRatio="none" aria-hidden="true">
    <polygon fill="var(--cyan)" points="0,965 690,965 900,1350 798,1350 738,1430 583,1178 0,1178"/>
    <polygon fill="var(--grey)" points="798,1350 1413,1350 1438,1390 1438,1708 850,1708 870,1660 738,1430"/>
    <polygon fill="var(--grey)" points="800,1788 1438,1788 1438,1860 755,1860"/>
    <rect fill="var(--cyan)" x="0" y="1708" width="1438" height="80"/>
  </svg>

  <div class="pictorial pictorial--pipes" role="img" aria-label="Blue and grey plastic plumbing pipes"></div>
  <div class="pictorial pictorial--mascot" role="img" aria-label="Cartoon plumber in blue overalls holding a pipe wrench"></div>

  <h1>
    <span class="headline headline--top">IN NEED OF</span>
    <span class="headline headline--accent">PLUMBING</span>
    <span class="headline headline--bottom">EXPERTS?</span>
  </h1>

  <div class="address">
    <svg width="38" height="56" viewBox="0 0 38 56" aria-hidden="true">
      <path d="M19 0C8.5 0 0 8.5 0 19c0 13 19 37 19 37s19-24 19-37C38 8.5 29.5 0 19 0z" fill="var(--white)"/>
      <circle cx="19" cy="19" r="8" fill="var(--ink)"/>
    </svg>
    <p>Your Address<br>Here</p>
  </div>

  <div class="call">
    <div class="call__label">
      <svg width="38" height="38" viewBox="0 0 38 38" aria-hidden="true">
        <circle cx="19" cy="19" r="19" fill="var(--white)"/>
        <path d="M12 9l5 5-3 3c1.5 3 4 5.5 7 7l3-3 5 5-3 4c-8 0-17-9-17-17z" fill="var(--cyan)"/>
      </svg>
      CALL NOW!
    </div>
    <div class="call__number">1800-555 0199</div>
  </div>

  <section class="services">
    <h2>OUR SERVICES</h2>
    <ul>
      <li><svg width="28" height="28" viewBox="0 0 28 28" aria-hidden="true"><circle cx="13" cy="15" r="11" fill="none" stroke="var(--white)" stroke-width="2.5"/><path d="M7 14l6 6L26 4" fill="none" stroke="var(--cyan)" stroke-width="4" stroke-linecap="round"/></svg>Hot water issues</li>
      <li><svg width="28" height="28" viewBox="0 0 28 28" aria-hidden="true"><circle cx="13" cy="15" r="11" fill="none" stroke="var(--white)" stroke-width="2.5"/><path d="M7 14l6 6L26 4" fill="none" stroke="var(--cyan)" stroke-width="4" stroke-linecap="round"/></svg>Burst Pipes</li>
      <li><svg width="28" height="28" viewBox="0 0 28 28" aria-hidden="true"><circle cx="13" cy="15" r="11" fill="none" stroke="var(--white)" stroke-width="2.5"/><path d="M7 14l6 6L26 4" fill="none" stroke="var(--cyan)" stroke-width="4" stroke-linecap="round"/></svg>Gas Plumbing</li>
      <li><svg width="28" height="28" viewBox="0 0 28 28" aria-hidden="true"><circle cx="13" cy="15" r="11" fill="none" stroke="var(--white)" stroke-width="2.5"/><path d="M7 14l6 6L26 4" fill="none" stroke="var(--cyan)" stroke-width="4" stroke-linecap="round"/></svg>Roof leaks</li>
      <li><svg width="28" height="28" viewBox="0 0 28 28" aria-hidden="true"><circle cx="13" cy="15" r="11" fill="none" stroke="var(--white)" stroke-width="2.5"/><path d="M7 14l6 6L26 4" fill="none" stroke="var(--cyan)" stroke-width="4" stroke-linecap="round"/></svg>Drain blockages</li>
      <li class="more">and so much more</li>
    </ul>
  </section>

  <div class="logo" aria-label="Clearflow Plumbing Solutions">
    <span>CLEARFLOW</span>
    <span>PLUMBING</span>
    <span>SOLUTIONS</span>
  </div>

  <footer class="footer">
    <div class="footer__item">
      <svg width="22" height="22" viewBox="0 0 22 22" aria-hidden="true"><circle cx="11" cy="11" r="11" fill="var(--ink)"/><rect x="5" y="7" width="12" height="8" fill="none" stroke="var(--cyan)" stroke-width="1.5"/><path d="M5 7l6 5 6-5" fill="none" stroke="var(--cyan)" stroke-width="1.5"/></svg>
      HELLO@CLEARFLOWPLUMBING.COM
    </div>
    <div class="footer__divider"></div>
    <div class="footer__item">
      <svg width="22" height="22" viewBox="0 0 22 22" aria-hidden="true"><circle cx="11" cy="11" r="11" fill="var(--ink)"/><circle cx="11" cy="11" r="6" fill="none" stroke="var(--cyan)" stroke-width="1.4"/><path d="M5 11h12M11 5c-3 3-3 9 0 12M11 5c3 3 3 9 0 12" fill="none" stroke="var(--cyan)" stroke-width="1.2"/></svg>
      WWW.CLEARFLOWPLUMBING.COM
    </div>
  </footer>
</main>
</body>
</html>
```